Northfield Energy Product Distribution Brochure

We are looking to have our current brochure for our customers completely redesigned...the idea is to present the relevant information in an attractive way . Our website is northfieldenergy-example.com where you can find more information about us. We have included a file with a rough idea of the page order and what each should include but feel free to adapt based on design. The example provided is only for context and doesnt have to be maintained. We will be using the brochure both digitally and in print form. As long as it reads easily and is eye catching, the design can be horizontal or vertical.Final deliverable should be indesign file.

"Our Brands" page: should be limited to one page (space being enough) where it has the header for each one (for example diesel generators) space for one or two lines of text and then the corresponding logos for each of the five categories
Updates

For those asking: the "our brands" page should be a single page layout where there is a header with the corresponding section and space for maybe one line of text followed by the two logos for that category. Each of the product pages should be similar in fashion to the one in the document attached: a photo of the product with some white space and space for the text to be included. We will be posting additional examples today

Target Market(s)

We want to present it to customers both digitally and in print so they can see our products

Industry/Entity Type

Power Generation

Font styles to use
Serif

Requirements
Must have
• Eye catching and able to present the information in a presentable fashion. Rest is up to you.
Nice to have
• Should incorporate the colors of our logo but can also add other depending on design

```html
<!DOCTYPE html>
<html lang="en">
<head>
<meta charset="utf-8">
<title>Northfield Energy – Product Brochure Spread</title>
<link href="https://fonts.googleapis.com/css2?family=Archivo+Black&family=Montserrat:wght@400;500;600&display=swap" rel="stylesheet">
<style>
  :root{
    --bg-light:#d0d1d3;
    --bg-dark:#8a8a8c;
    --yellow:#f5b800;
    --yellow-bright:#ffe100;
    --ink:#231f20;
    --band:#3f3a3b;
    --white:#ffffff;
    --photo-warm-a:#3a3532;
    --photo-warm-b:#8a7a6c;
    --photo-night-a:#15161c;
    --photo-night-b:#4a4030;
  }
  *{margin:0;padding:0;box-sizing:border-box}
  html,body{width:1200px;height:801px;overflow:hidden}
  body{position:relative;background:var(--bg-light);font-family:"Montserrat",sans-serif;color:var(--ink)}
  .backdrop{position:absolute;inset:0}
  .spread{position:absolute;left:78px;top:80px;width:1034px;height:669px;overflow:hidden}
  .page{position:absolute;top:0;width:517px;height:669px}
  .page--left{left:0}
  .page--right{left:517px;background:var(--white)}
  .photo{position:absolute}
  .photo--gears{inset:0;background:linear-gradient(135deg,var(--photo-warm-a) 0%,#6e625a 45%,var(--photo-warm-b) 75%,#5a4a40 100%)}
  .card{position:absolute;top:183px;height:478px;background:var(--white)}
  .card--one{left:0;width:258px}
  .card--two{left:271px;width:246px}
  .kicker{position:absolute;left:37px;top:60px;color:var(--white);font-weight:600;font-size:20px;letter-spacing:.5px}
  .kicker-rule{position:absolute;left:37px;top:80px;width:47px;height:4px;background:var(--yellow)}
  .title{position:absolute;left:36px;top:88px;font-family:"Archivo Black",sans-serif;font-size:40px;color:var(--yellow);letter-spacing:.5px;white-space:nowrap}
  .product-shot{position:absolute}
  .product-shot--regulator{left:124px;top:135px;width:116px;height:138px;background:linear-gradient(160deg,#2c2f35,#4d5560);transform:rotate(-6deg)}
  .product-shot--module{left:320px;top:141px;width:112px;height:114px;background:linear-gradient(160deg,#c9cbcd,#f1f1f1)}
  .product-name{position:absolute;top:272px;font-weight:500;font-size:19px;line-height:25px;letter-spacing:.8px;color:var(--yellow)}
  .body-copy{position:absolute;font-size:9px;line-height:11.15px;color:var(--ink)}
  .col-a{left:37px}.col-b{left:332px}
  .body-copy.col-a,.body-copy.col-b{top:331px;width:152px}
  .page-number{position:absolute;top:632px;width:84px;height:37px}
  .page-number span{position:absolute;left:26px;top:5px;font-family:"Archivo Black",sans-serif;font-size:21px;color:var(--ink)}
  .page-number--left{left:0}
  .page-number--right{left:517px}
  .band{position:absolute;left:0;top:661px;width:1034px;height:8px;background:var(--band)}
  .right-art{position:absolute;left:0;top:0}
  .right-page .kicker,.right-page .kicker-rule,.right-page .title{left:36px}
  .controller-shot{position:absolute;left:252px;top:154px;width:218px;height:163px;border-radius:8px;background:linear-gradient(170deg,#2a2b2e,#111214)}
  .brand-chip{position:absolute;left:158px;top:255px;width:60px;height:60px;background:#000;display:flex;align-items:center;justify-content:center;color:var(--white);font-family:"Montserrat",sans-serif;font-weight:600;font-size:9px;letter-spacing:.5px}
  .desc-heading{position:absolute;left:44px;top:341px;font-size:14.5px;letter-spacing:.6px;color:var(--yellow)}
  .body-copy.desc{left:44px;top:367px;width:178px}
  .body-copy.side-1{left:259px;top:399px;width:222px}
  .body-copy.side-2{left:259px;top:515px;width:222px}
  .chevrons{position:absolute;left:0;top:0;pointer-events:none}
</style>
</head>
<body>
<svg class="backdrop" width="1200" height="801" viewBox="0 0 1200 801" aria-hidden="true">
  <polygon points="0,616 1200,321 1200,801 0,801" fill="var(--bg-dark)"/>
</svg>

<main class="spread">
  <section class="page page--left">
    <div class="photo photo--gears" role="img" aria-label="Close-up photograph of alternator gears and machined metal parts"></div>
    <p class="kicker">OUR PRODUCT</p>
    <div class="kicker-rule"></div>
    <h1 class="title">ALTERNATOR PARTS</h1>
    <div class="card card--one"></div>
    <div class="card card--two"></div>
    <div class="product-shot product-shot--regulator" role="img" aria-label="Product photo of an automatic voltage regulator circuit board"></div>
    <div class="product-shot product-shot--module" role="img" aria-label="Product photo of a current boost system module"></div>

    <h2 class="product-name col-a">PRODUCT<br>NAME</h2>
    <p class="body-copy col-a">Lorem ipsum dolor sit amet, consectetuer adipiscing elit, sed diam nonummy nibh euismod tincidunt ut laoreet dolore magna aliquam erat volutpat. Ut wisi enim ad minim veniam, quis nostrud exerci tation ullamcorper suscipit lobortis nisl ut aliquip ex ea commodo consequat. Duis autem vel eum iriure dolor in hendrerit in vulputate velit esse molestie consequat, vel illum dolore eu feugiat nulla facilisis at vero eros et accumsan et iusto odio dignissim qui blandit praesent luptatum zzril delenit augue duis dolore te feugait nulla facilisi.</p>

    <h2 class="product-name col-b">PRODUCT<br>NAME</h2>
    <p class="body-copy col-b">Lorem ipsum dolor sit amet, consectetuer adipiscing elit, sed diam nonummy nibh euismod tincidunt ut laoreet dolore magna aliquam erat volutpat. Ut wisi enim ad minim veniam, quis nostrud exerci tation ullamcorper suscipit lobortis nisl ut aliquip ex ea commodo consequat. Duis autem vel eum iriure dolor in hendrerit in vulputate velit esse molestie consequat, vel illum dolore eu feugiat nulla facilisis at vero eros et accumsan et iusto odio dignissim qui blandit praesent luptatum zzril delenit augue duis dolore te feugait nulla facilisi.</p>
  </section>

  <section class="page page--right right-page">
    <svg class="right-art" width="517" height="669" viewBox="0 0 517 669">
      <defs>
        <linearGradient id="nightPlant" x1="0" y1="0" x2="1" y2="1">
          <stop offset="0" stop-color="var(--photo-night-a)"/>
          <stop offset="0.6" stop-color="#2a2a2c"/>
          <stop offset="1" stop-color="var(--photo-night-b)"/>
        </linearGradient>
      </defs>
      <polygon role="img" aria-label="Photograph of an industrial power plant at dusk" points="0,0 517,0 517,131 0,327" fill="url(#nightPlant)"/>
      <polygon points="72,300 517,62 517,131 0,327" fill="var(--yellow-bright)"/>
      <polygon points="0,327 517,131 517,140 0,327" fill="var(--white)"/>
    </svg>
    <p class="kicker">OUR PRODUCT</p>
    <div class="kicker-rule"></div>
    <h1 class="title">CONTROLLERS</h1>
    <div class="controller-shot" role="img" aria-label="Product photo of a generator control module with display and buttons"></div>
    <div class="brand-chip">VEXMONT</div>

    <h2 class="desc-heading">DESCRIPTION</h2>
    <p class="body-copy desc">Lorem ipsum dolor sit amet, consectetuer adipiscing elit, sed diam nonummy nibh euismod tincidunt ut laoreet dolore magna aliquam erat volutpat. Ut wisi enim ad minim veniam, quis nostrud exerci tation ullamcorper suscipit lobortis nisl ut aliquip ex ea commodo consequat. Duis autem vel eum iriure dolor in hendrerit in vulputate velit esse molestie consequat, vel illum dolore eu feugiat nulla facilisis at vero eros et accumsan et iusto odio dignissim qui blandit praesent luptatum zzril delenit augue duis dolore te feugait nulla facilisi.</p>
    <p class="body-copy side-1">Lorem ipsum dolor sit amet, consectetuer adipiscing elit, sed diam nonummy nibh euismod tincidunt ut laoreet dolore magna aliquam erat volutpat. Ut wisi enim ad minim veniam, quis nostrud exerci tation ullamcorper suscipit lobortis nisl ut aliquip ex ea commodo consequat. Duis autem vel eum iriure dolor in hendrerit in vulputate velit esse molestie consequat.</p>
    <p class="body-copy side-2">Lorem ipsum dolor sit amet, consectetuer adipiscing elit, sed diam nonummy nibh euismod tincidunt ut laoreet dolore magna aliquam erat volutpat. Ut wisi enim ad minim veniam, quis nostrud exerci tation ullamcorper suscipit lobortis nisl ut aliquip ex ea commodo consequat. Duis autem vel eum iriure dolor in hendrerit in vulputate velit esse molestie consequat.</p>
  </section>

  <svg class="chevrons" width="1034" height="669" viewBox="0 0 1034 669" aria-hidden="true">
    <polyline points="386,665 565,552 770,665" fill="none" stroke="var(--yellow)" stroke-width="7"/>
    <polyline points="437,665 604,561 790,665" fill="none" stroke="var(--band)" stroke-width="7"/>
  </svg>

  <div class="band"></div>

  <div class="page-number page-number--left">
    <svg width="84" height="37" viewBox="0 0 84 37" aria-hidden="true">
      <defs><linearGradient id="tabA" x1="0" x2="1"><stop offset="0" stop-color="var(--yellow)"/><stop offset="1" stop-color="var(--yellow-bright)"/></linearGradient></defs>
      <polygon points="15,0 84,0 62,37 0,37" fill="url(#tabA)"/>
    </svg>
    <span>10</span>
  </div>
  <div class="page-number page-number--right">
    <svg width="84" height="37" viewBox="0 0 84 37" aria-hidden="true">
      <polygon points="22,0 84,0 62,37 0,37" fill="url(#tabA)"/>
    </svg>
    <span>11</span>
  </div>
</main>
</body>
</html>
```